Postcard Design

Marlow Painting-all types of painting and staining-house,deck and roof powerwashing-stone and masonry sealing-
30 years in business-licensed and insured
Ray Pettibone
pettiboneworks@brushmail.example
9145820731

Industry/Entity Type

Painting

```html
<!DOCTYPE html>
<html lang="en">
<head>
<meta charset="utf-8">
<title>Marlow Painting Postcard</title>
<link rel="stylesheet" href="https://fonts.googleapis.com/css2?family=Anton&family=Permanent+Marker&display=swap">
<style>
  :root {
    --page: #ffffff;
    --ink: #111111;
    --red: #b3141c;
    --maroon: #8e1515;
    --blue: #3a2f9a;
    --purple: #3d2a86;
    --yellow: #ffe11a;
    --tan: #d8cba4;
    --white: #ffffff;
    --brand: #4b3c8f;
  }
  * { margin: 0; padding: 0; box-sizing: border-box; }
  html, body { width: 791px; height: 1200px; overflow: hidden; background: var(--page); }
  body { position: relative; font-family: "Anton", "Arial Narrow", sans-serif; color: var(--ink); }

  .postcard {
    position: absolute; left: 36px; width: 718px; background: var(--white); overflow: hidden;
    box-shadow: 0 2px 6px rgba(0,0,0,0.35);
  }
  .postcard--front { top: 36px; height: 558px; }
  .postcard--back { top: 627px; height: 556px; }

  /* Brand name block */
  .brand { position: absolute; display: flex; align-items: center; gap: 10px; }
  .brand__mark { width: 16px; height: 16px; background: var(--red); flex: none; }
  .brand__name { font-size: 28px; color: var(--brand); letter-spacing: 1px; line-height: 1.05; }
  .postcard--front .brand { left: 26px; top: 40px; }
  .postcard--back .brand { left: 470px; top: 432px; }

  /* Front */
  .headline-banner {
    position: absolute; left: 207px; top: 0; width: 511px; height: 72px;
    background: var(--yellow); display: flex; align-items: center; justify-content: center;
    font-size: 32px; font-style: italic; letter-spacing: 0.5px; white-space: nowrap;
  }
  .headline-banner__of { font-size: 26px; }
  .hl-red { color: var(--red); }
  .hl-blue { color: var(--blue); }

  .paint-photo {
    position: absolute; left: 0; top: 125px; width: 470px; height: 433px;
    background: linear-gradient(180deg, #f2efe9 0%, #c9a47a 40%, #e24a2a 62%, #f0c12c 78%, #f4f4f4 100%);
  }

  .contact-blob {
    position: absolute; left: 160px; top: 142px; width: 280px; height: 94px;
    background: var(--maroon); border-radius: 40px 18px 44px 22px;
    color: var(--white); text-align: center; padding-top: 10px;
    font-family: "Permanent Marker", "Anton", cursive;
  }
  .contact-blob__name { font-size: 16px; line-height: 1.3; }
  .contact-blob__tel { font-size: 22px; line-height: 1.3; }
  .contact-blob__email { font-size: 11px; line-height: 1.5; }

  .experience-badge { position: absolute; left: 14px; top: 284px; width: 176px; height: 160px; }
  .experience-badge__text {
    position: absolute; inset: 0; display: flex; flex-direction: column;
    align-items: center; justify-content: center; color: var(--red); line-height: 0.95;
  }
  .experience-badge__num { font-size: 40px; }
  .experience-badge__yrs { font-size: 30px; }
  .experience-badge__exp { font-size: 13px; color: var(--white); background: var(--red); padding: 2px 6px; margin-top: 4px; }

  .service-panel {
    position: absolute; left: 450px; top: 146px; width: 250px; height: 395px;
    background: var(--purple); color: var(--white); text-align: center;
    font-family: "Permanent Marker", "Anton", cursive; padding-top: 22px;
  }
  .service-panel__lg { font-size: 32px; line-height: 1.35; }
  .service-panel__xl { font-size: 42px; line-height: 1.25; }
  .service-panel__md { font-size: 21px; line-height: 1.5; }
  .service-panel__sm { font-size: 16px; line-height: 1.3; margin-top: 8px; }
  .service-panel__xs { font-size: 11px; margin-top: 16px; opacity: 0.8; }

  /* Back */
  .brush-photo {
    position: absolute; left: 0; top: 0; width: 718px; height: 272px;
    background: linear-gradient(160deg, #f6f1e6 0%, #e8d3a0 35%, #c8402a 55%, #b8a890 75%, #f3ede0 100%);
  }
  .tagline-band {
    position: absolute; left: 0; top: 272px; width: 718px; height: 128px;
    background: linear-gradient(180deg, #e6dcbd 0%, var(--tan) 100%);
    display: flex; align-items: center; justify-content: center; overflow: hidden;
  }
  .tagline-band__text {
    display: inline-block; font-size: 56px; white-space: nowrap;
    transform: scaleX(0.72); transform-origin: center;
  }
  .tagline-band__of { font-size: 46px; }
  .phone-line {
    position: absolute; left: 28px; top: 466px; display: flex; align-items: center; gap: 14px;
    font-size: 50px; line-height: 1;
  }
  .phone-line svg { width: 80px; height: 50px; }
</style>
</head>
<body>

<section class="postcard postcard--front">
  <div class="paint-photo" role="img" aria-label="Photo of open paint jars in red, blue, yellow and green with a paint roller and tray"></div>

  <div class="brand">
    <span class="brand__mark"></span>
    <span class="brand__name">MARLOW<br>PAINTING</span>
  </div>

  <div class="headline-banner">ALL TYPES&nbsp;<span class="headline-banner__of">OF</span>&nbsp;<span class="hl-red">PAINTING</span>&nbsp;AND&nbsp;<span class="hl-blue">STAINING</span></div>

  <div class="contact-blob">
    <div class="contact-blob__name">CALL RAY PETTIBONE</div>
    <div class="contact-blob__tel">TEL: 9145820731</div>
    <div class="contact-blob__email">PETTIBONEWORKS@BRUSHMAIL.EXAMPLE</div>
  </div>

  <div class="experience-badge">
    <svg viewBox="0 0 176 160" width="176" height="160" aria-hidden="true">
      <polygon fill="#3d2a86" points="88,0 102,24 128,8 130,38 160,32 148,60 176,74 150,92 166,118 136,120 136,150 110,136 92,160 76,136 48,152 46,122 16,124 30,96 0,80 28,62 14,34 44,38 46,8 72,22"/>
      <circle cx="88" cy="80" r="56" fill="#ffffff"/>
    </svg>
    <div class="experience-badge__text">
      <span class="experience-badge__num">30+</span>
      <span class="experience-badge__yrs">YEARS</span>
      <span class="experience-badge__exp">EXPERIENCE</span>
    </div>
  </div>

  <div class="service-panel">
    <div class="service-panel__lg">PAINTING</div>
    <div class="service-panel__lg">STAINING</div>
    <div class="service-panel__xl">HOUSE</div>
    <div class="service-panel__md">DECK AND ROOF</div>
    <div class="service-panel__md">POWER WASHING</div>
    <div class="service-panel__sm">STONE AND MASONRY<br>SEALING</div>
    <div class="service-panel__xs">LICENSED AND INSURED</div>
  </div>
</section>

<section class="postcard postcard--back">
  <div class="brush-photo" role="img" aria-label="Photo of assorted paint brushes with wooden and red handles"></div>

  <div class="tagline-band">
    <span class="tagline-band__text">ALL TYPES <span class="tagline-band__of">OF</span> <span class="hl-red">PAINTING</span> AND <span class="hl-blue">STAINING</span></span>
  </div>

  <div class="phone-line">
    <svg viewBox="0 0 82 52" aria-hidden="true">
      <path fill="#111" d="M4 18 C4 4 78 4 78 18 L78 24 L60 24 L58 16 L24 16 L22 24 L4 24 Z"/>
      <path fill="#111" d="M22 24 L60 24 L70 48 L12 48 Z"/>
      <circle cx="41" cy="36" r="7" fill="#fff"/>
    </svg>
    <span>914-582-0731</span>
  </div>

  <div class="brand">
    <span class="brand__mark"></span>
    <span class="brand__name">MARLOW<br>PAINTING</span>
  </div>
</section>

</body>
</html>
```